Letterhead and matching envelope design for a dental office

We need a new stationary design, letterhead and envelope #10, for a dental office in Denver area. We are called Brightfield Dental. We want a simple and minimalistic design but not a boring design. I wish to have one good point that makes it look professional. I have attached our logo. Feel free to use either one. I want the design for letterhead and envelope look like a "matching pair" but not look the same. The envelope doesn't have to be white and it will have an address window on bottom left.

Target Market(s)

everyone who visits dentist (adults)

Industry/Entity Type

Dental

Font styles to use
Other font styles liked:
• close to font on logo or something that matches well

Requirements
Must have
• professional
• simple, minimalistic
• unique point that stands out
Nice to have
• matching but not same design for letterhead and envelope
Should not have
• not look like all the other boring designs
• no flowery, distracting feats

```html
<!DOCTYPE html>
<html lang="en">
<head>
<meta charset="utf-8">
<title>Brightfield Dental Letterhead</title>
<link href="https://fonts.googleapis.com/css2?family=Lato:wght@400;700&family=Satisfy&display=swap" rel="stylesheet">
<style>
  :root {
    --backdrop: #e9e7e3;
    --paper: #ffffff;
    --ink: #2b2b2b;
    --ink-soft: #4a4a4a;
    --brand-green: #3cb54a;
    --band-pale: #b9dfb4;
    --leaf-tint: #eef5ea;
    --signature-blue: #2a2a8c;
  }
  * { box-sizing: border-box; margin: 0; padding: 0; }
  html, body {
    width: 1112px; height: 1200px; overflow: hidden;
    background: var(--backdrop);
    font-family: "Lato", sans-serif;
    color: var(--ink);
  }
  .letterhead {
    position: absolute; left: 214px; top: 88px;
    width: 696px; height: 985px;
    background: var(--paper);
    box-shadow: 0 2px 10px rgba(0,0,0,.18);
    overflow: hidden;
  }
  .letterhead > * { position: absolute; }
  .brand-mark {
    top: 64px; left: 0; width: 100%;
    display: flex; justify-content: center; align-items: center; gap: 8px;
    color: var(--brand-green); font-size: 22px; font-weight: 700;
    letter-spacing: .5px;
  }
  .brand-dot { width: 12px; height: 12px; border-radius: 50%; background: var(--brand-green); }
  .backdrop-decoration { left: 90px; top: 520px; }
  .letter-body {
    left: 36px; top: 255px; width: 625px;
    font-size: 14.5px; line-height: 18.2px; color: var(--ink-soft);
  }
  .salutation { font-weight: 700; font-size: 15px; margin-bottom: 22px; }
  .letter-body p.paragraph { text-align: justify; margin-bottom: 18px; }
  .closing { left: 36px; top: 620px; font-size: 14.5px; line-height: 18px; color: var(--ink); }
  .signature {
    font-family: "Satisfy", cursive; font-size: 26px; color: var(--signature-blue);
    margin: 6px 0 14px;
  }
  .footer-address { left: 36px; top: 889px; font-size: 14px; line-height: 19.5px; color: var(--ink); }
  .footer-address .company { color: var(--brand-green); }
  .footer-contact { left: 263px; top: 907px; font-size: 14px; line-height: 20px; }
  .contact-row { display: flex; align-items: center; gap: 6px; }
  .footer-web {
    right: 35px; top: 942px; font-size: 14px; color: var(--brand-green);
    background: var(--paper); padding: 0 6px;
  }
  .band-thin { left: 0; top: 951px; width: 100%; height: 7px; background: var(--band-pale); }
  .band-thick { left: 0; top: 960px; width: 100%; height: 25px; background: var(--brand-green); }
</style>
</head>
<body>
  <main class="letterhead">
    <div class="brand-mark"><span class="brand-dot"></span>Brightfield Dental</div>

    <svg class="backdrop-decoration" width="520" height="440" role="img" aria-label="Faint brand decoration area">
      <circle cx="270" cy="240" r="190" fill="var(--leaf-tint)"/>
    </svg>

    <section class="letter-body">
      <p class="salutation">Dear Mr. John,</p>
      <p class="paragraph">Lorem Ipsum is simply dummy text of the printing and typesetting industry. Lorem Ipsum has been the industry's standard dummy text ever since the 1500s, when an unknown printer took a galley of type and scrambled it to make a type specimen book. It has survived not only five centuries, but also the leap into electronic typesetting, remaining essentially unchanged.</p>
      <p class="paragraph">The standard chunk of Lorem Ipsum used since the 1500s is reproduced below for those interested. Sections 1.10.32 and 1.10.33 from "de Finibus Bonorum et Malorum" by Cicero are also reproduced in their exact original form, accompanied by English versions from the 1914 translation by H. Rackham</p>
      <p class="paragraph">Lorem Ipsum is simply dummy text of the printing and typesetting industry. Lorem Ipsum has been the industry's standard dummy text ever since the 1500s, when an unknown printer took a galley of type and scrambled it to make a type specimen book. It has survived not only five centuries, but also the leap into electronic typesetting, remaining essentially unchanged. It was popularised in the</p>
    </section>

    <section class="closing">
      <p>Sincerely Your,</p>
      <p class="signature">your name</p>
      <p>Name Last Name</p>
      <p>Company Name</p>
    </section>

    <address class="footer-address" style="font-style:normal">
      <div class="company">Brightfield Dental</div>
      <div>2275 Maple Ridge Dr,</div>
      <div>Suite 210 Arvada, CO 80002</div>
    </address>

    <div class="footer-contact">
      <div class="contact-row">
        <svg width="15" height="15" viewBox="0 0 16 16" aria-hidden="true"><circle cx="8" cy="8" r="8" fill="var(--brand-green)"/><path d="M5.2 4.2l1.3-.3.8 1.8-.9.7a5 5 0 0 0 2.3 2.3l.7-.9 1.8.8-.3 1.3c-3 .4-6.1-2.7-5.7-6z" fill="#fff"/></svg>
        <span>720-555-0142</span>
      </div>
      <div class="contact-row">
        <svg width="15" height="15" viewBox="0 0 16 16" aria-hidden="true"><circle cx="8" cy="8" r="8" fill="var(--brand-green)"/><rect x="4" y="5.2" width="8" height="5.6" fill="#fff"/><path d="M4 5.2l4 3 4-3" stroke="var(--brand-green)" stroke-width=".9" fill="none"/></svg>
        <span>info@brightfielddental.com</span>
      </div>
    </div>

    <div class="band-thin"></div>
    <div class="footer-web">www.brightfielddental.com</div>
    <div class="band-thick"></div>
  </main>
</body>
</html>
```